Venture Capital Firm Needs Website Redesign

We need a bold revamp of our website (https://halvenmoor.vc/)
which at the moment looks washed out. We want a crisp, fresh and unique look. Feel free to keep as much or as little content in the site. The only thing we need to keep is a team section. The site should convey a clear distinction between our 3 product lines: Venture Capital, Private Credit, and Crypto. Two versions of our logo are attached and they should not change. For design inspirations, we like http://www.plumridgecap.com/ for a more simple site and for a more built out site we like http://tallowgate.com/

Updates
Industry/Entity Type
Investment
Coding
Coded - Design and coding required
Number of Pages Required
1 page
Font styles to use
Colors
Designer to choose colors to be used in the design.
Requirements
Must have
- - Clear distinction between our 3 product lines: Venture Capital, Private Credit
- - Team section

Nice to have
- Some really creative aspect like http://www.plumridgecap.com/ has with the distinction between first, second, and third kind

```html
<!DOCTYPE html>
<html lang="en">
<head>
<meta charset="utf-8">
<title>Halvenmoor</title>
<link href="https://fonts.googleapis.com/css2?family=Open+Sans:wght@300;400;600;700&display=swap" rel="stylesheet">
<style>
:root{
  --green:#93a93a;
  --green-dark:#7d9230;
  --ink:#2f2f2f;
  --text:#4a4a4a;
  --muted:#8a8a8a;
  --line:#e3e3e3;
  --dark:#262626;
  --field:#ececec;
  --white:#ffffff;
  --accent:#e06a2c;
}
*{box-sizing:border-box;margin:0;padding:0}
html,body{width:1200px;height:5187px;overflow:hidden}
body{position:relative;background:var(--white);font-family:"Open Sans",Arial,sans-serif;color:var(--text);font-size:14px;line-height:1.55}
.abs{position:absolute}
.hero{left:0;top:0;width:1200px;height:710px;
  background:
    radial-gradient(ellipse 420px 260px at 560px 330px,rgba(214,176,150,.55),rgba(214,176,150,0) 70%),
    radial-gradient(ellipse 500px 300px at 980px 260px,rgba(150,170,188,.55),rgba(150,170,188,0) 70%),
    linear-gradient(180deg,#f4f5f6 0%,#dfe3e6 35%,#cfd5da 60%,#f3f4f5 100%)}
.hero-fade{left:0;top:430px;width:1200px;height:280px;background:linear-gradient(180deg,rgba(255,255,255,0),rgba(255,255,255,.85) 55%,rgba(255,255,255,.95))}
.topbar{left:622px;top:0;width:578px;height:50px;background:var(--green);border-bottom-left-radius:26px;display:flex;align-items:center;gap:22px;padding-left:70px;color:var(--white);font-size:12px;font-weight:600}
.topbar .item{display:flex;align-items:center;gap:7px}
.topbar .dot{width:22px;height:22px;border:1.5px solid var(--white);border-radius:50%}
.topbar .socials{display:flex;gap:8px;margin-left:10px}
.brand{left:42px;top:68px;font-size:40px;font-weight:300;letter-spacing:1px;color:var(--ink);line-height:1}
.nav{left:398px;top:86px;display:flex;gap:22px;font-size:12.5px;font-weight:600;color:var(--ink);letter-spacing:.3px}
.nav a{color:inherit;text-decoration:none;display:flex;align-items:center;gap:6px}
.nav .ico{width:12px;height:12px;border:1.5px solid currentColor;border-radius:3px}
.nav a.active{color:var(--green);border-bottom:2px solid var(--green);padding-bottom:4px}
.hero-title{left:0;top:490px;width:1200px;text-align:center;font-size:38px;font-weight:300;color:var(--ink);line-height:1.3}
.hl{color:var(--green)}
.btn{display:flex;align-items:center;justify-content:center;color:var(--white);font-weight:600;text-decoration:none}
.btn-green{left:484px;top:612px;width:232px;height:46px;background:var(--green);border-radius:4px;font-size:18px}
.btn-dark{height:36px;width:205px;background:var(--dark);border-radius:3px;font-size:12.5px}
.sec-title{display:flex;align-items:center;gap:12px;font-size:19px;font-weight:300;letter-spacing:1.5px;color:var(--ink);text-transform:uppercase}
.sec-title .mark{width:38px;height:38px;border:2px solid var(--green);border-radius:50%}
.center{left:0;width:1200px;justify-content:center}
.para{font-size:14px;line-height:1.65;color:var(--text)}
.about-text{left:104px;top:890px;width:996px;text-align:center}
.divider{left:0;width:1200px;height:1px;background:var(--line)}
.photo-circle{border-radius:50%;border:10px solid #f2f2f2;box-shadow:0 8px 22px rgba(0,0,0,.18)}
.reflection{border-radius:50%;filter:blur(6px);opacity:.25}
.logos{display:flex;align-items:center;gap:40px}
.logo-name{font-weight:700;font-size:26px;color:var(--ink);line-height:1}
.logo-name.sm{font-size:14px;letter-spacing:1px}
.credit{left:0;top:1653px;width:1200px;height:478px;background:linear-gradient(135deg,#3a3c3f 0%,#232427 60%,#2d2f33 100%)}
.credit .sec-title{color:var(--white)}
.credit-text{left:80px;top:1795px;width:1040px;text-align:center;color:#e8e8e8}
.team-card{width:232px;text-align:center}
.avatar{width:212px;height:212px;margin:0 auto;border-radius:50%;border:8px solid #eeeeee;box-shadow:0 6px 16px rgba(0,0,0,.15);
  background:radial-gradient(circle at 50% 42%,#d9b9a2 0%,#c49a80 26%,#e9eaeb 48%,#f6f6f6 70%),linear-gradient(180deg,#f5f5f5,#d7d9db)}
.avatar.active{border-color:var(--green)}
.team-name{margin-top:14px;font-size:15px;font-weight:600;color:var(--ink)}
.team-role{font-size:14px;color:var(--green)}
.team-social{display:flex;justify-content:center;gap:10px;margin-top:14px}
.team-social span{width:14px;height:14px;background:#c9c9c9;border-radius:3px}
.arrow{font-size:34px;color:var(--ink);font-weight:300;line-height:1}
.blog{left:0;top:3302px;width:1200px;height:979px;background:linear-gradient(160deg,#3d4044 0%,#26282b 60%,#303236 100%)}
.blog .sec-title{color:var(--white)}
.post{background:var(--white);padding:22px 24px;box-shadow:0 4px 14px rgba(0,0,0,.25)}
.post .date{font-size:13px;font-weight:700;color:var(--green-dark)}
.post .head{font-size:13.5px;font-weight:700;color:var(--ink);line-height:1.4}
.post .body{font-size:12.5px;color:var(--muted);line-height:1.5;margin-top:4px}
.post .go{width:22px;height:22px;border-radius:50%;background:var(--accent);color:#fff;display:flex;align-items:center;justify-content:center;font-size:12px;margin-top:12px}
.view-all{left:899px;top:3908px;width:225px;height:276px;background:var(--green);color:var(--white);font-weight:700;font-size:17px;letter-spacing:1px}
.field{background:var(--field);height:48px;padding:13px 16px;font-size:13.5px;color:var(--ink)}
.footer{left:0;top:4858px;width:1200px;height:294px;background:var(--green);color:var(--white)}
.copyright{left:0;top:5152px;width:1200px;height:35px;background:var(--green-dark);color:var(--white);font-size:10.5px;display:flex;align-items:center;justify-content:center;letter-spacing:.5px}
.f-head{font-size:13px;font-weight:700;letter-spacing:1px;margin-bottom:14px}
.f-col{top:4905px;font-size:12.5px;line-height:1.6;color:var(--white)}
.f-row{display:flex;align-items:center;gap:10px;margin-bottom:12px}
.f-ico{width:22px;height:22px;border:1.5px solid var(--white);border-radius:50%;flex:none}
</style>
</head>
<body>

<div class="abs hero" role="img" aria-label="Photo of hands working on a laptop with financial charts, soft grey tones"></div>
<div class="abs hero-fade"></div>

<div class="abs topbar">
  <div class="item">
    <svg width="14" height="14" viewBox="0 0 24 24"><path fill="#fff" d="M6.6 10.8a15 15 0 0 0 6.6 6.6l2.2-2.2c.3-.3.7-.4 1-.2 1.1.4 2.3.6 3.6.6.6 0 1 .4 1 1V20c0 .6-.4 1-1 1A17 17 0 0 1 3 4c0-.6.4-1 1-1h3.5c.6 0 1 .4 1 1 0 1.3.2 2.5.6 3.6.1.3 0 .7-.2 1z"/></svg>
    1-800-555-0142
  </div>
  <div class="item">
    <svg width="14" height="14" viewBox="0 0 24 24"><rect x="2" y="5" width="20" height="14" rx="1" fill="none" stroke="#fff" stroke-width="2"/><path d="M2 6l10 7 10-7" fill="none" stroke="#fff" stroke-width="2"/></svg>
    hello@halvenmoor.vc
  </div>
  <div class="socials"><span class="dot"></span><span class="dot"></span><span class="dot"></span></div>
</div>

<div class="abs brand">HALVENMOOR</div>

<nav class="abs nav">
  <a class="active" href="#about"><span class="ico"></span>ABOUT</a>
  <a href="#vc"><span class="ico"></span>VENTURE CAPITAL</a>
  <a href="#credit"><span class="ico"></span>PRIVATE CREDIT</a>
  <a href="#crypto"><span class="ico"></span>CRYPTO</a>
  <a href="#team"><span class="ico"></span>TEAM</a>
  <a href="#blog"><span class="ico"></span>BLOG</a>
  <a href="#contact"><span class="ico"></span>CONTACT</a>
</nav>

<h1 class="abs hero-title"><span class="hl">Halvenmoor</span> operates at the intersection of <span class="hl">technology</span><br>and <span class="hl">novel asset classes</span>.</h1>
<a class="abs btn btn-green" href="#about">Get Started</a>

<!-- About -->
<h2 class="abs sec-title center" id="about" style="top:800px"><span class="mark"></span>About <span class="hl">Halvenmoor</span></h2>
<p class="abs para about-text">Halvenmoor operates three businesses that bridge technology and finance. We invest in pre-seed venture capital, and build software for the companies we invest in. We manage direct private credit funds that provide private capital to alternative private credit platforms, enabling them to finance the loans they originate. We create crypto funds for individuals, RIAs and institutions to get simple and easy access to cryptocurrencies.</p>
<a class="abs btn btn-dark" href="#vc" style="left:498px;top:1012px">Learn More</a>
<div class="abs divider" style="top:1140px"></div>

<!-- Venture Capital -->
<h2 class="abs sec-title" id="vc" style="left:76px;top:1236px"><span class="mark"></span>Venture <span class="hl">Capital</span></h2>
<p class="abs para" style="left:76px;top:1322px;width:670px">Halvenmoor invests in early-stage startups led by founders who are passionate and knowledgeable about the markets they serve. We have our own software developers and product managers. We work with the founders in our portfolio to help them bring products to market, earning equity for this work and for the cash we invest in their companies.</p>
<div class="abs logos" style="left:76px;top:1485px">
  <span class="logo-name sm">MARLOW GROUP</span>
  <span class="logo-name sm">SABLEKIT</span>
  <span class="logo-name">Tinyroam</span>
  <span class="logo-name">Boardline</span>
</div>
<div class="abs reflection" style="left:830px;top:1560px;width:242px;height:40px;background:#5c6b78"></div>
<div class="abs photo-circle" style="left:795px;top:1232px;width:312px;height:312px;background:radial-gradient(ellipse at 70% 40%,rgba(120,190,235,.7),rgba(120,190,235,0) 40%),linear-gradient(165deg,#eef1f3 0%,#b8c3cb 35%,#2e3a46 62%,#151b22 100%)" role="img" aria-label="Photo of a businessman in a dark suit with a rising blue chart graphic"></div>

<!-- Private Credit -->
<section class="abs credit" id="credit">
  <h2 class="abs sec-title center" style="top:92px"><span class="mark"></span>Private <span class="hl">Credit</span></h2>
</section>
<p class="abs para credit-text">Halvenmoor Private Credit provides capital to lending businesses that are focused on using technology to establish new credit markets, create new credit products or dramatically re-invent an existing form of credit. We believe that the pioneers who build something truly different in a credit market will create the most sustainable business models. Given our heritage as a venture firm, we are comfortable with emerging businesses and can provide capital for a company's first loan.</p>
<div class="abs logos" style="left:0;top:1975px;width:1200px;justify-content:center;gap:60px">
  <span class="logo-name" style="color:#fff">Ferrow Lending</span>
  <span class="logo-name" style="color:#fff">Sprouta</span>
  <span class="logo-name" style="color:#fff">Brightledger</span>
</div>

<!-- Crypto -->
<div class="abs reflection" style="left:116px;top:2595px;width:260px;height:40px;background:#3d7a1c"></div>
<div class="abs photo-circle" style="left:76px;top:2240px;width:340px;height:340px;background:radial-gradient(circle at 50% 35%,#d9ff8a 0%,#7fc23a 25%,#2f6e1a 55%,#0b220a 100%)" role="img" aria-label="Illustration of a glowing green digital currency circuit"></div>
<h2 class="abs sec-title" id="crypto" style="left:501px;top:2222px"><span class="mark"></span>Crypto</h2>
<p class="abs para" style="left:501px;top:2300px;width:640px">Halvenmoor Crypto is a multi-strategy cryptocurrency asset management firm.</p>
<p class="abs para" style="left:501px;top:2345px;width:640px">The Halvenmoor Crypto Index tracks the top 15 cryptocurrencies weighted by market cap and rebalanced twice a month. We believe this is the simplest and most cost effective way to obtain cryptocurrency exposure. Our process has been designed by experts from financial services and cryptocurrency industries.</p>
<a class="abs btn btn-dark" href="#team" style="left:501px;top:2470px">Learn More</a>
<div class="abs divider" style="top:2645px"></div>

<!-- Team -->
<h2 class="abs sec-title center" id="team" style="top:2732px"><span class="mark"></span>Our <span class="hl">Team</span></h2>
<p class="abs" style="left:0;top:2822px;width:1200px;text-align:center;font-size:15px;color:var(--ink)">The very best helping the very best.</p>
<div class="abs arrow" style="left:78px;top:2975px">&#8249;</div>
<div class="abs arrow" style="left:1105px;top:2975px">&#8250;</div>
<div class="abs" style="left:136px;top:2885px;display:flex">
  <div class="team-card"><div class="avatar active" role="img" aria-label="Portrait photo of a partner"></div><div class="team-name">Ravi Osten</div><div class="team-role">Partner</div><div class="team-social"><span></span><span></span><span></span><span></span></div></div>
  <div class="team-card"><div class="avatar" role="img" aria-label="Portrait photo of a partner"></div><div class="team-name">Tomas Veld</div><div class="team-role">Partner</div><div class="team-social"><span></span><span></span><span></span><span></span></div></div>
  <div class="team-card"><div class="avatar" role="img" aria-label="Portrait photo of a partner"></div><div class="team-name">Elan Mercer</div><div class="team-role">Partner</div><div class="team-social"><span></span><span></span><span></span><span></span></div></div>
  <div class="team-card"><div class="avatar" role="img" aria-label="Portrait photo of a partner"></div><div class="team-name">Owen Harlow</div><div class="team-role">Partner</div><div class="team-social"><span></span><span></span><span></span><span></span></div></div>
</div>

<!-- Blog -->
<section class="abs blog" id="blog">
  <h2 class="abs sec-title center" style="top:86px"><span class="mark"></span>From Our <span class="hl">Blog</span></h2>
</section>
<div class="abs" style="left:76px;top:3479px;width:425px;height:411px;background:radial-gradient(ellipse at 55% 55%,rgba(70,140,205,.55),rgba(70,140,205,0) 45%),linear-gradient(135deg,#f1f4f7 0%,#c9d6e2 45%,#8fa4b8 100%)" role="img" aria-label="Photo of hands holding a tablet showing financial charts"></div>
<article class="abs post" style="left:501px;top:3479px;width:623px;height:186px">
  <div class="date">October 03, 2017</div>
  <div class="head">Lorem ipsum dolor sit amet, consectetur adipiscing elit.</div>
  <div class="body">Sed diam nonummy nibh euismod tincidunt ut laoreet dolore magna aliquam erat volutpat. Ut wisi enim ad minim veniam, quis nostrud exerci tation ullamcorper.</div>
  <div class="go">&#8594;</div>
</article>
<div class="abs" style="left:840px;top:3665px;width:284px;height:225px;background:radial-gradient(ellipse at 40% 45%,rgba(225,225,225,.55),rgba(225,225,225,0) 45%),linear-gradient(135deg,#8a96a2 0%,#3e4954 55%,#1f262e 100%)" role="img" aria-label="Photo of colleagues reviewing documents at a desk"></div>
<article class="abs post" style="left:501px;top:3690px;width:339px;height:200px">
  <div class="date">October 24, 2017</div>
  <div class="head">Lorem ipsum dolor sit amet, consectetur.</div>
  <div class="body">Sed diam nonummy nibh euismod tincidunt ut laoreet dolore magna aliquam erat.</div>
  <div class="go">&#8594;</div>
</article>
<article class="abs post" style="left:76px;top:3908px;width:294px;height:276px">
  <div class="date">October 19, 2017</div>
  <div class="head">Lorem ipsum dolor sit amet</div>
  <div class="body">Sed diam nonummy nibh euismod tincidunt ut laoreet dolore magna.</div>
  <div class="go">&#8594;</div>
</article>
<div class="abs" style="left:370px;top:3908px;width:529px;height:276px;background:radial-gradient(ellipse at 55% 50%,rgba(110,190,240,.6),rgba(110,190,240,0) 50%),linear-gradient(135deg,#3f6e93 0%,#1d3c58 50%,#0b1a29 100%)" role="img" aria-label="Photo of hands on a tablet with a glowing digital network overlay"></div>
<a class="abs btn view-all" href="#blog">VIEW ALL NEWS</a>

<!-- Contact -->
<h2 class="abs sec-title center" id="contact" style="top:4374px"><span class="mark"></span>Contact <span class="hl">Us</span></h2>
<p class="abs" style="left:0;top:4450px;width:1200px;text-align:center;font-size:15px;color:var(--ink)">We would love to hear from you.</p>
<div class="abs field" style="left:121px;top:4523px;width:304px">Your Name</div>
<div class="abs field" style="left:450px;top:4523px;width:304px">Your Email</div>
<div class="abs field" style="left:778px;top:4523px;width:304px">Your Subject</div>
<div class="abs field" style="left:121px;top:4585px;width:961px;height:128px">Message</div>
<a class="abs btn btn-dark" href="#contact" style="left:498px;top:4732px">SUBMIT</a>

<!-- Footer -->
<footer class="abs footer">
  <div class="abs" style="left:76px;top:50px;width:208px;height:208px;border:3px solid #fff;border-radius:50%"></div>
</footer>
<div class="abs f-col" style="left:311px">
  <div class="f-head">QUICK LINKS</div>
  <div>Venture Capital</div><div>Private Credit</div><div>Crypto</div><div>About</div><div>Team</div><div>Blog</div><div>Contact</div>
</div>
<div class="abs f-col" style="left:474px;width:220px">
  <div class="f-head">CONTACT</div>
  <div class="f-row"><span class="f-ico"></span><span>Halvenmoor<br>88 Quarry Street, Suite 410<br>Northgate, NY 10090</span></div>
  <div class="f-row"><span class="f-ico"></span><span>1-800-555-0142</span></div>
  <div class="f-row"><span class="f-ico"></span><span>hello@halvenmoor.vc</span></div>
</div>
<div class="abs f-col" style="left:716px">
  <div class="f-head">FOLLOW US</div>
  <div class="f-row"><span class="f-ico"></span><span>Pagebook</span></div>
  <div class="f-row"><span class="f-ico"></span><span>Chirper</span></div>
  <div class="f-row"><span class="f-ico"></span><span>Linkwork</span></div>
</div>
<div class="abs f-col" style="left:875px">
  <div class="f-head">NEWSLETTER</div>
  <div style="display:flex">
    <div style="width:165px;height:38px;background:#fff;color:var(--ink);font-size:12px;padding:10px 12px">Enter Email Address</div>
    <div style="width:95px;height:38px;background:var(--dark);color:#fff;font-size:12px;font-weight:700;display:flex;align-items:center;justify-content:center">SIGN UP</div>
  </div>
</div>
<div class="abs copyright">COPYRIGHT © 2018 HALVENMOOR. ALL RIGHTS RESERVED.</div>

</body>
</html>
```